Quillmere Tax Advisers Business Card

We are seeking a clean, professional, and modern double sided business card design for Quillmere Tax Advisers, a tax, accounting, and advisory firm serving business owners, professionals, and investors.
The design should convey credibility, precision, trust, and sophistication appropriate for a CPA level tax advisory firm. Avoid playful, trendy, or overly decorative styles. The look should be sharp, balanced, and timeless.
Our official company logo has been uploaded, which must be incorporated appropriately and consistently with the brand. Designers should not modify, distort, or recreate the logo.
Card format
Standard US business card size (3.5 x 2 inches)
Double sided
Design direction
Professional and modern
Minimalist and uncluttered
Strong typography and clean spacing
Subtle visual interest is welcome, but simplicity is preferred
High contrast and readability are critical
Front side
Primary focus on the Quillmere Tax Advisers logo
The firm name should be clearly legible and visually prominent
Background may be white or dark, depending on what best complements the logo
Back side
Contact information layout, such as
Name: Martin G. Pellow, MSA, CFP®, AIF®, EA
Title: Managing Director, Tax
Email: mpellow@myquillmerefirm.net
Website: https://www.corvelfirm-example.tax/
Mobile: (480) 555-0132
Direct: (817) 555-0187
Main: (817) 555-0149
Address: 3807 Fenwick Rd., Suite 118, Grapevine, TX 76099
Icons may be used sparingly if they enhance clarity
The layout should feel organized and structured
Color and style
Use colors that complement the uploaded logo
Neutral, professional tones preferred
Avoid loud or saturated colors
The design should print well on standard cardstock
Print considerations
Design should be print‑ready
No edge to edge elements that risk being cut off
Proper margins and bleed awareness
Overall, the goal is a polished, high end business card that reflects trust, expertise, and professionalism consistent with a firm providing tax strategy, compliance, and advisory services.

```html
<!DOCTYPE html>
<html lang="en">
<head>
<meta charset="utf-8">
<title>Quillmere Tax Advisers – Business Card</title>
<link rel="stylesheet" href="https://fonts.googleapis.com/css2?family=Montserrat:wght@400;500;700&display=swap">
<style>
  :root {
    --backdrop: #262626;
    --card: #ffffff;
    --navy: #1f2559;
    --ink: #1c1c22;
    --accent: #f47530;
  }
  * { margin: 0; padding: 0; box-sizing: border-box; }
  html, body { width: 1200px; height: 1200px; overflow: hidden; }
  body {
    background: var(--backdrop);
    position: relative;
    font-family: "Montserrat", sans-serif;
  }
  .card {
    position: absolute;
    left: 179px;
    width: 861px;
    height: 496px;
    background: var(--card);
    overflow: hidden;
  }
  .card--front { top: 84px; }
  .card--back  { top: 621px; }

  .firm-name {
    position: absolute;
    left: 0; right: 0;
    top: 208px;
    text-align: center;
    font-weight: 700;
    font-size: 46px;
    letter-spacing: 1px;
    color: var(--navy);
  }

  .person-name {
    position: absolute;
    left: 41px; top: 39px;
    font-weight: 700;
    font-size: 27.5px;
    letter-spacing: 0.3px;
    color: var(--navy);
  }
  .person-title {
    position: absolute;
    left: 40px; top: 78px;
    font-weight: 400;
    font-size: 27px;
    color: var(--ink);
  }
  .contact-list {
    position: absolute;
    left: 43px; top: 171px;
    list-style: none;
  }
  .contact-item {
    display: flex;
    align-items: center;
    height: 40px;
    font-size: 29px;
    color: var(--ink);
  }
  .contact-item:last-child { height: 34px; }
  .contact-icon {
    width: 26px; height: 24px;
    margin-right: 12px;
    fill: var(--navy);
    flex: none;
  }
  .firm-details {
    position: absolute;
    left: 41px; top: 349px;
    font-style: normal;
    font-size: 26px;
    line-height: 38px;
    color: var(--ink);
  }
  .web-highlight { color: var(--accent); }
</style>
</head>
<body>

<section class="card card--front">
  <p class="firm-name">Quillmere Tax Advisers</p>
</section>

<section class="card card--back">
  <h1 class="person-name">Martin G. Pellow, MSA, CFP®, AIF®, EA</h1>
  <p class="person-title">Managing Director, Tax</p>

  <ul class="contact-list">
    <li class="contact-item">
      <svg class="contact-icon" viewBox="0 0 24 24" aria-hidden="true"><path d="M6.6 10.8c1.4 2.8 3.8 5.1 6.6 6.6l2.2-2.2c.3-.3.7-.4 1-.2 1.1.4 2.3.6 3.6.6.6 0 1 .4 1 1V20c0 .6-.4 1-1 1C10.6 21 3 13.4 3 4c0-.6.4-1 1-1h3.5c.6 0 1 .4 1 1 0 1.3.2 2.5.6 3.6.1.3 0 .7-.2 1l-2.3 2.2z"/></svg>
      (480) 555-0132
    </li>
    <li class="contact-item">
      <svg class="contact-icon" viewBox="0 0 24 24" aria-hidden="true"><path d="M2 8c0-2 4.5-4 10-4s10 2 10 4v2h-5V8.5c-1.5-.5-3.2-.7-5-.7s-3.5.2-5 .7V10H2V8zm5 3h10l3 4v5H4v-5l3-4zm5 1.5a2.5 2.5 0 1 0 0 5 2.5 2.5 0 0 0 0-5z"/></svg>
      (817) 555-0187
    </li>
    <li class="contact-item">
      <svg class="contact-icon" viewBox="0 0 24 24" aria-hidden="true"><path d="M2 8c0-2 4.5-4 10-4s10 2 10 4v2h-5V8.5c-1.5-.5-3.2-.7-5-.7s-3.5.2-5 .7V10H2V8zm5 3h10l3 4v5H4v-5l3-4zm5 1.5a2.5 2.5 0 1 0 0 5 2.5 2.5 0 0 0 0-5z"/></svg>
      (817) 555-0149
    </li>
    <li class="contact-item">
      <svg class="contact-icon" viewBox="0 0 24 24" aria-hidden="true"><path d="M2 5h20v14H2V5zm2 2v.4l8 5.3 8-5.3V7H4zm0 2.8V17h4.6L4 9.8zm16 0L15.4 17H20V9.8zM10.4 13.9 7.1 17h9.8l-3.3-3.1-1.6 1-1.6-1z"/></svg>
      mpellow@myquillmerefirm.net
    </li>
  </ul>

  <address class="firm-details">
    www.<span class="web-highlight">quillmerefirm-example</span>.tax<br>
    3807 Fenwick Rd., Suite 118,<br>
    Grapevine, TX 76099
  </address>
</section>

</body>
</html>
```